Real estate investor, needing a business card that communicates warmth, integrity, empathy.

I have a logo that can be manipulated to align with the message - "Serving your home selling needs." Want it to stand out from typical real estate investor cards, and make distressed home sellers feel a connection with me. Should communicate warmth, integrity, empathy, and trustworthiness.

Target Market(s)

Distressed home owners who need to sell their homes, not using realtors.

Contact Information for Business Card

Glossy front and matte back, with a small box that is labelled "notes." I like darker blues and blacks together, but doesn't have to be, as long as it communicates trustworthiness, and a strong call to action.

Other font styles liked:
• see "must haves" above, but willing to review whatever comes my way.

Requirements
Must have
• The fonts on my logo are Aviano, Lusitana, and Marcellus. We don't have to use those, but I favor them.

```html
<!DOCTYPE html>
<html lang="en">
<head>
<meta charset="utf-8">
<title>Ridgeline Home Partners – Business Card</title>
<link href="https://fonts.googleapis.com/css2?family=Marcellus&family=Roboto:wght@400;500&display=swap" rel="stylesheet">
<style>
  :root {
    --stage: #1f1d1e;
    --card-navy: #0c2244;
    --ink-white: #ffffff;
  }
  * { margin: 0; padding: 0; box-sizing: border-box; }
  html, body {
    width: 1200px; height: 1200px; overflow: hidden;
    background: var(--stage);
  }
  .sheet { position: relative; width: 1200px; height: 1200px; }
  .card {
    position: absolute;
    width: 700px; height: 400px;
    background: var(--card-navy);
    border-radius: 26px;
    color: var(--ink-white);
    box-shadow: 0 18px 40px rgba(0,0,0,0.55);
  }
  /* front */
  .card--front { left: 110px; top: 150px; }
  .brand {
    position: absolute; left: 0; right: 0; top: 110px;
    text-align: center;
    font-family: "Marcellus", serif;
    font-size: 40px; line-height: 52px; letter-spacing: 2px;
    color: var(--ink-white);
  }
  .notes {
    position: absolute; left: 150px; top: 300px;
    display: flex; align-items: center; gap: 16px;
  }
  .notes__label {
    font-family: "Roboto", sans-serif; font-weight: 500;
    font-size: 17px; letter-spacing: 0.5px;
  }
  .notes__field { width: 440px; height: 30px; background: var(--ink-white); }
  /* back */
  .card--back { left: 390px; top: 650px; }
  .identity {
    position: absolute; right: 372px; top: 170px;
    text-align: right;
    font-family: "Roboto", sans-serif;
  }
  .identity__name { font-weight: 500; font-size: 30px; letter-spacing: 0.5px; }
  .identity__role { font-weight: 400; font-size: 18px; margin-top: 2px; }
  .divider {
    position: absolute; left: 348px; top: 120px;
    width: 2px; height: 170px; background: var(--ink-white);
  }
  .contact {
    position: absolute; left: 370px; top: 118px;
    list-style: none;
    font-family: "Roboto", sans-serif; font-size: 16px;
    line-height: 22px;
  }
  .contact__item { display: flex; align-items: flex-start; gap: 10px; margin-bottom: 4px; }
  .contact__item--address { margin-bottom: 10px; }
  .contact__icon { width: 16px; height: 16px; margin-top: 3px; flex: none; }
</style>
</head>
<body>
<main class="sheet">

  <section class="card card--front" aria-label="Card front">
    <div class="brand">Ridgeline<br>Home Partners</div>
    <div class="notes">
      <span class="notes__label">NOTES</span>
      <span class="notes__field"></span>
    </div>
  </section>

  <section class="card card--back" aria-label="Card back">
    <div class="identity">
      <div class="identity__name">MARCUS HALE</div>
      <div class="identity__role">Principal Broker</div>
    </div>
    <div class="divider"></div>
    <ul class="contact">
      <li class="contact__item contact__item--address">
        <svg class="contact__icon" viewBox="0 0 16 16"><path d="M8 1a5 5 0 0 0-5 5c0 4 5 9 5 9s5-5 5-9a5 5 0 0 0-5-5zm0 7a2 2 0 1 1 0-4 2 2 0 0 1 0 4z" fill="#fff"/></svg>
        <span>1847 Spruce Hollow Road<br>Northfield, AK 99512</span>
      </li>
      <li class="contact__item">
        <svg class="contact__icon" viewBox="0 0 16 16"><path d="M4 1.5l2.2 3-1.4 1.6a8 8 0 0 0 5.1 5.1l1.6-1.4 3 2.2-1.2 2.5C7 14.5 1.5 9 1.5 2.7z" fill="#fff"/></svg>
        <span>907.555.0142</span>
      </li>
      <li class="contact__item">
        <svg class="contact__icon" viewBox="0 0 16 16"><rect x="4" y="1" width="8" height="14" rx="1.5" fill="none" stroke="#fff" stroke-width="1.5"/><circle cx="8" cy="12.5" r="0.9" fill="#fff"/></svg>
        <span>907.555.0187</span>
      </li>
      <li class="contact__item">
        <svg class="contact__icon" viewBox="0 0 16 16"><rect x="1" y="3" width="14" height="10" fill="none" stroke="#fff" stroke-width="1.5"/><path d="M1 3l7 6 7-6" fill="none" stroke="#fff" stroke-width="1.5"/></svg>
        <span>hello@ridgelinehomes.example</span>
      </li>
      <li class="contact__item">
        <svg class="contact__icon" viewBox="0 0 16 16"><circle cx="8" cy="8" r="6.5" fill="none" stroke="#fff" stroke-width="1.3"/><ellipse cx="8" cy="8" rx="2.8" ry="6.5" fill="none" stroke="#fff" stroke-width="1.1"/><path d="M1.5 8h13" stroke="#fff" stroke-width="1.1"/></svg>
        <span>www.ridgelinehomes.example</span>
      </li>
    </ul>
  </section>

</main>
</body>
</html>
```